Web Design Project - Beachwear Affiliate Website needs an eyedropping look!

Hello,
I need a website design that incorporates a logo design as well for an affiliate site that features beachwear including swimwear, coverups, hats, bags, etc. I want it to have the look and feel of an ecommerce site but without the shopping cart so when the visitor gets to the purchase/buy button, they will be sent to the partner via affiliate link in a new window. This is a site targeting women's beachwear so I'm looking for a soft color palette.
LOGO: Looking for a beautiful text based logo with elegant fonts. The Site Logo should read "Shoreline Parade" with possibly some sort of break element between the two words. Possibly two different colors for each word. Please no beach type elements such as sun, umbrella, etc. Just nice and clean.
This requires 4 distinct page levels/designs. All pages should have navigation to the other categories without paging backwards.
Main Page - Large picture window in the top center. I would like this to be a slider rotating various pictures. 4 smaller picture spaces specials or products should be underneath the main picture. One should be designed in the style of the site with a text box reading "Weekly Specials".
Main Menu's for the following product categories: Home, Bikinis, One Piece Swimsuits, Modest Swimwear, Beach Cover Ups, Beach Hats & Bags, Specialty Swimwear, About Sizing) For Menu categories above that require subcategories, I'd like a mouseover effect to show the subcategories so users can bypass the subcategories page through direct navigation. Smaller links in the top right or bottom center for About Us, Contact, & Partners.
Subcategory Page - For Bikinis, Modest Swimwear, and Specialty Swimwear, I need a subcategory page offering image based sub-categories with text. The top of each of these pages should have space for text content. Please use filler text in your designs to get a sense for look. It can say anything or just be jibberish in your example. I will provide the subcategories in a separate uploaded file but as an example, Bikinis will have categories like String Bikinis, Brazilian Bikinis, G-string Bikini's etc. (Note Images should be sized to 200w x 312h pixels)
Category Page - This will be the main image gallery page for each category/subcategory. Images with ability to add pricing text underneath. Two buttons per image: More Info & Purchase. Purchase will take them to an external website utilizing affiliate links in a new window. More Info or clicking on the picture will take you to the product page. (Note images should be sized to 200w x 312h pixels
Product Page - Larger image sized to 420w x 629h with space for a product description to the right along with space to add sizing information as needed. Purchase button will take user to external website utilizing affiliate links in a new window.
All,
Target Market(s)
Women 21-50 searching for Beachwear
Industry/Entity Type
Shopping
Requirements
Must have
- Please see details in the project description. Pages need to be able to be easily SEO'd and incorporate search engine friendly urls.
Simplicity in updating or adding product pages or additional categories is essential.
Social Network Integrated buttons for Chirply, Pagemeet, and Vexa Circle throughout the site.
Nice to have
- I'd really like to integrate a blog posting page so that I can add unique written content for the search engines.
Should not have
- Shopping cart/Ecommerce
Dark Color Palette

```html
<!DOCTYPE html>
<html lang="en">
<head>
<meta charset="utf-8">
<title>Shoreline Parade</title>
<link rel="stylesheet" href="https://fonts.googleapis.com/css2?family=Antonio:wght@200;300&family=Open+Sans:wght@400;600;700&display=swap">
<style>
:root{
  --aqua:#22c3dc;
  --aqua-dark:#1aa6bd;
  --mint:#1fc99a;
  --orange:#f58a3c;
  --coral:#fd935e;
  --green:#22df7a;
  --lilac:#c08de8;
  --ink:#6b6b6b;
  --soft:#8d8d8d;
  --rule:#f1efec;
  --page-bg:#ececea;
  --white:#fff;
}
*{margin:0;padding:0;box-sizing:border-box}
html,body{width:720px;height:1200px;overflow:hidden;background:var(--page-bg)}
body{font-family:"Open Sans",Arial,sans-serif;color:var(--ink)}
.stage{position:relative;width:780px;height:1300px;transform:scale(.923077);transform-origin:0 0}
.abs{position:absolute}
.sheet{left:65px;top:32px;width:650px;height:1203px;background:var(--white);box-shadow:0 0 4px rgba(0,0,0,.12)}
.brand{left:86px;top:56px;font-size:20px;font-weight:400;color:var(--orange);letter-spacing:-.5px}
.tagline{left:87px;top:82px;font-size:8.5px;color:var(--soft)}
.util-links{top:83px;right:88px;display:flex;gap:14px;font-size:7.5px;color:var(--ink)}
.main-nav{left:84px;top:104px;width:611px;height:32px;background:var(--aqua);display:flex;align-items:center;padding-left:14px;gap:0}
.main-nav span{color:var(--white);font-size:8.5px;padding:5px 7px;white-space:nowrap}
.main-nav .active{background:var(--aqua-dark);margin:0 2px}
.hero{left:84px;top:149px;width:611px;height:325px;background:linear-gradient(180deg,#3a9fe0 0%,#8cc7ee 45%,#5fc6d8 70%,#e9e3d6 78%,#f3eee6 100%)}
.ribbon{left:117px;top:149px;width:143px;height:240px}
.ribbon-text{left:117px;top:180px;width:143px;color:var(--white);padding-left:13px}
.season{font-family:"Antonio",sans-serif;font-weight:300;font-size:40px;letter-spacing:11px;line-height:44px}
.collection{font-family:"Antonio",sans-serif;font-weight:300;font-size:40px;line-height:44px;letter-spacing:.5px}
.ribbon-rule{width:117px;height:5px;background:rgba(255,255,255,.25);margin:10px 0 8px}
.offer-lead{font-size:12px;line-height:14px}
.offer{font-size:20px;font-weight:700;line-height:22px}
.dots{left:97px;top:455px;display:flex;gap:7px}
.dots i{width:6px;height:6px;border-radius:50%;background:#f5b400}
.dots i.on{background:var(--mint)}
.dropdown{left:520px;top:143px;width:123px;height:97px;background:var(--aqua);padding:10px 0 0 10px}
.dropdown p{color:var(--white);font-size:8px;line-height:19.5px}
.welcome{left:65px;top:498px;width:650px;text-align:center;font-family:"Antonio",sans-serif;font-weight:200;font-size:42px;color:var(--aqua);letter-spacing:-.5px}
.intro{left:130px;top:558px;width:520px;text-align:center;font-size:9.3px;line-height:15.5px;color:var(--ink)}
.section-title{left:84px;top:616px;font-size:14.5px;font-weight:700;color:var(--aqua)}
.rule{left:84px;width:611px;height:6px;background:var(--rule)}
.product{top:663px;width:143px}
.product-photo{height:163px}
.product-tag{height:51px;background:var(--aqua);color:var(--white);padding:9px 0 0 14px}
.product-name{font-size:9px;font-weight:700;line-height:12px}
.product-price{font-size:14px;font-weight:700;line-height:20px}
.promo{top:891px;width:195px;height:64px;color:var(--white);padding:8px 0 0 13px}
.promo-title{font-family:"Antonio",sans-serif;font-weight:300;font-size:27px;line-height:30px}
.promo-sub{font-size:8.5px;line-height:12px}
.foot-col{top:995px;width:190px}
.foot-col h3{font-size:12px;font-weight:400;color:var(--aqua);margin-bottom:12px}
.foot-col p{font-size:8.3px;line-height:15.5px;color:var(--ink)}
.foot-col .list p{line-height:19.5px}
.social{display:flex;gap:8px;margin:17px 0 9px}
.social span{display:flex;align-items:center;gap:3px;font-size:6.5px;color:var(--ink)}
.social b{width:15px;height:15px;display:block}
.contact-line{font-size:8.5px;font-weight:700;color:var(--soft);line-height:13px}
.contact-line small{font-weight:400;font-size:7.5px}
.legal{left:85px;top:1190px;font-size:7.5px;line-height:12px;color:var(--ink)}
.foot-brand{right:87px;top:1195px;font-size:15px;color:var(--soft);letter-spacing:-.4px}
</style>
</head>
<body>
<div class="stage">
  <div class="abs sheet"></div>

  <div class="abs brand">Shoreline Parade</div>
  <div class="abs tagline">One stop solution for beachwares &amp; accessories</div>
  <div class="abs util-links"><span>ABOUT US</span><span>CONTACT</span><span>PARTNERS</span></div>

  <nav class="abs main-nav">
    <span>Home</span><span>Bikinis</span><span>One piece Swimsuits</span><span>Modest Swimwear</span><span>Beach Cover Ups</span><span>Beach Hats&amp; Bags</span><span class="active">Specialty Swimwear</span><span>About sizing</span>
  </nav>

  <div class="abs hero" role="img" aria-label="Slider photo: woman in a yellow bikini and straw hat lounging on a beach chair on white sand beside a woven bag, blue sky and sea behind"></div>

  <svg class="abs ribbon" viewBox="0 0 143 240" aria-hidden="true"><polygon points="0,0 143,0 143,210 71.5,240 0,210" fill="var(--mint)"/></svg>
  <div class="abs ribbon-text">
    <div class="season">SUMMER</div>
    <div class="collection">COLLECTIONS</div>
    <div class="ribbon-rule"></div>
    <div class="offer-lead">GET UPTO</div>
    <div class="offer">50% OFF</div>
  </div>
  <div class="abs dots"><i></i><i></i><i class="on"></i><i></i><i></i></div>

  <div class="abs dropdown">
    <p>Plus Size Swimwear</p><p>SPF Protection Swimwear</p><p>Tan Through Swimwear</p><p>Daring Swimwear</p>
  </div>

  <h1 class="abs welcome">WELCOME TO SHORELINE PARADE</h1>
  <p class="abs intro">Sed scelerisque felis et massa venenatis fermentum! Aenean convallis mattis blandit! Sed ac mauris ut sapien porttitor facilisis. Nulla sit amet ornare justo. Proin dictum dolor ut enim convallis porta. Nullam malesuada ante vitae.</p>

  <h2 class="abs section-title">WEEKLY SPECIALS</h2>
  <div class="abs rule" style="top:644px"></div>

  <div class="abs product" style="left:84px">
    <div class="product-photo" role="img" aria-label="Product photo: model in a blue bandeau bikini and sunglasses" style="background:linear-gradient(160deg,#8fc6e6,#d9b49c)"></div>
    <div class="product-tag"><div class="product-name">AENEAN CONVALLIS</div><div class="product-price">$150</div></div>
  </div>
  <div class="abs product" style="left:240px">
    <div class="product-photo" role="img" aria-label="Product photo: model in a wide straw sun hat" style="background:linear-gradient(160deg,#e8eef3,#c9a898)"></div>
    <div class="product-tag"><div class="product-name">MALESUADA SAGITTIS</div><div class="product-price">$120</div></div>
  </div>
  <div class="abs product" style="left:397px">
    <div class="product-photo" role="img" aria-label="Product photo: model in a black bikini top with beaded necklace" style="background:linear-gradient(160deg,#f4efe9,#b98f74)"></div>
    <div class="product-tag"><div class="product-name">AENEAN CONVALLIS</div><div class="product-price">$150</div></div>
  </div>
  <div class="abs product" style="left:553px">
    <div class="product-photo" role="img" aria-label="Product photo: model in a fedora and sunglasses against a blue sky" style="background:linear-gradient(160deg,#2f8fe0,#9ed0f2)"></div>
    <div class="product-tag"><div class="product-name">MAURIS TRISTIQUE</div><div class="product-price">$230</div></div>
  </div>

  <div class="abs promo" style="left:84px;background:var(--coral)"><div class="promo-title">SOME BANNER</div><div class="promo-sub">SOME TEXT FOR BANNER</div></div>
  <div class="abs promo" style="left:292px;background:var(--green)"><div class="promo-title">SOME BANNER</div><div class="promo-sub">SOME TEXT FOR BANNER</div></div>
  <div class="abs promo" style="left:500px;background:var(--lilac)"><div class="promo-title">SOME BANNER</div><div class="promo-sub">SOME TEXT FOR BANNER</div></div>

  <div class="abs rule" style="top:968px"></div>

  <div class="abs foot-col" style="left:85px">
    <h3>ABOUT US</h3>
    <p>Mauris in felis justo. Aliquam sed arcu sed lectus ultricies viverra eget eget turpis! Maecenas tincid-unt, urna a hendrerit tempor, urnara eget eget turpis! Maecenas tincidunt, urna a hendrerit tempor, urna sapien dignissim enim, non luctusa dolor jus sapien dignissim enim, non luctusa dolor justo ut lorem. Nullam mattis volutperos.</p>
  </div>
  <div class="abs foot-col" style="left:292px">
    <h3>POPULAR PRODUCTS</h3>
    <div class="list"><p>Maecenas tincidunt,</p><p>Burna a hendrerit tem</p><p>Alpor, urnara eget ege</p><p>Liturpis! Maecenas tincid</p><p>Bunt, urna a hendrerit temp</p><p>Tor, urna sapien</p></div>
  </div>
  <div class="abs foot-col" style="left:500px">
    <h3>CONNECT TO US</h3>
    <p>Taiverra eget eget turpis<br>&nbsp;Maecenas tincidunt<br>tempor, urnara, nas tin</p>
    <div class="social">
      <span><b style="background:#3b5a9a"></b>Pagemeet</span>
      <span><b style="background:#3fb6e8"></b>Chirply</span>
      <span><b style="background:#555"></b>Bookmarkly</span>
      <svg width="15" height="15" viewBox="0 0 15 15" aria-label="Feed"><rect width="15" height="15" rx="2" fill="#f28a1e"/><circle cx="4" cy="11" r="1.6" fill="#fff"/><path d="M3 7a5 5 0 0 1 5 5M3 3.5a8.5 8.5 0 0 1 8.5 8.5" stroke="#fff" stroke-width="1.6" fill="none"/></svg>
    </div>
    <div class="contact-line">CALL US - 1800555014</div>
    <div class="contact-line">MAIL US - <small>team@mail.example</small></div>
  </div>

  <div class="abs rule" style="top:1170px"></div>

  <div class="abs legal">Copyright website name - website descrption<br>Privacy policy - &nbsp;Disclaimer - &nbsp;Sitemap</div>
  <div class="abs foot-brand">Shoreline Parade</div>
</div>
</body>
</html>
```